Stretch on the Green with Mira

I want to advertise my Stretch on the Green classes for Summer. Classes are outside at the lovely local park. Holloway field. 83 Marangi St. Sandringham.
Classes are for beginners to advance levels.
Classes start Monday, October 17th.
Monday 6pm Beginners
Tuesday 6pm Intermediate
Thursday 6pm Intermediate/Advance
Saturday 9am All fitness levels
My Pilates classes are specially designed to help improve strength and flexibility but as well will also improve posture, reduce stress and develop control and endurance in the entire body.
Booking essential. Limited numbers so I can make sure the correct technique is always being followed.
For more info or to book contact details:
Mira 027358164
mira@corewithmira.net
www.corewithmira.net
$15 Per Session

Target Market(s)

Males and Females ages 35plus.

Industry/Entity Type

Fitness

Font styles to use
Sans Serif

Requirements
Must have
• My logo. Contact details. A Park that looks lovely to exercise at.
Nice to have
• Summer looking. Trees - inspiration to be exercising outside

```html
<!DOCTYPE html>
<html lang="en">
<head>
<meta charset="utf-8">
<title>Stretch on the Green with Mira – Summer Classes Flyer</title>
<link rel="stylesheet" href="https://fonts.googleapis.com/css2?family=Bebas+Neue&family=Montserrat:wght@400;500;600;700&display=swap">
<style>
  :root {
    --pink: #f284ad;
    --pink-deep: #ee6f9f;
    --charcoal: #4a4a4a;
    --charcoal-dark: #3e3e3e;
    --white: #ffffff;
    --paper: #f1f1f1;
    --text-grey: #555555;
    --stage: #eeeeee;
  }
  * { margin: 0; padding: 0; box-sizing: border-box; }
  html, body { width: 1200px; height: 2665px; overflow: hidden; background: var(--stage); }
  body { position: relative; font-family: "Montserrat", sans-serif; }

  .flyer {
    position: absolute; left: 102px; top: 627px;
    width: 996px; height: 1410px; overflow: hidden;
    background: var(--white);
    box-shadow: 0 4px 14px rgba(0,0,0,0.18);
  }
  .park-photo {
    position: absolute; left: 0; top: 0; width: 996px; height: 660px;
    background:
      linear-gradient(90deg, rgba(242,132,173,0.95) 0%, rgba(242,132,173,0.55) 30%, rgba(242,132,173,0) 55%),
      linear-gradient(180deg, #7fa9c4 0%, #c9d3cf 28%, #9bbf5e 48%, #7da646 75%, #6c9a3e 100%);
  }
  .class-photo {
    position: absolute; left: 50px; top: 640px; width: 900px; height: 640px;
    background: linear-gradient(180deg, #f4f4f4 0%, #e9e9e9 55%, #f2f2f2 100%);
  }
  .wave { position: absolute; left: 0; top: 500px; width: 996px; height: 200px; }

  .logo-disc {
    position: absolute; left: 32px; top: -155px; width: 432px; height: 432px;
    border-radius: 50%; background: var(--charcoal);
    border: 6px solid var(--white);
    display: flex; align-items: flex-end; justify-content: center; padding-bottom: 95px;
  }
  .logo-name {
    color: var(--pink); font-weight: 500; font-size: 27px;
    letter-spacing: 1px; text-transform: uppercase;
  }

  .headline {
    position: absolute; left: 53px; top: 330px;
    font-family: "Bebas Neue", sans-serif; color: var(--charcoal);
    font-size: 96px; line-height: 80px; letter-spacing: 0;
  }
  .season {
    position: absolute; left: 48px; top: 628px;
    font-family: "Bebas Neue", sans-serif; color: var(--charcoal);
    font-size: 70px; line-height: 70px;
  }
  .levels-ribbon { position: absolute; left: 53px; top: 711px; width: 475px; height: 67px; }
  .levels-text {
    position: absolute; left: 116px; top: 716px;
    color: var(--white); font-weight: 700; font-size: 22px; line-height: 28px; letter-spacing: 0.5px;
  }
  .benefits-intro {
    position: absolute; left: 113px; top: 810px; width: 370px;
    color: var(--pink); font-weight: 700; font-size: 22px; line-height: 26px;
    border-bottom: 2px solid var(--charcoal); padding-bottom: 2px;
  }
  .benefits { position: absolute; left: 116px; top: 884px; list-style: none; }
  .benefits li {
    position: relative; padding-left: 32px; margin-bottom: 21px;
    color: var(--charcoal); font-weight: 700; font-size: 21px; line-height: 24px; width: 400px;
  }
  .benefits svg { position: absolute; left: 0; top: 4px; width: 18px; height: 18px; }

  .schedule {
    position: absolute; left: 628px; top: 660px; width: 295px; height: 418px;
    background: var(--charcoal); border-radius: 0 0 12px 12px;
  }
  .start-strip {
    position: absolute; left: 0; top: 128px; width: 295px; height: 56px;
    background: var(--white); color: var(--charcoal);
    font-weight: 700; font-size: 17px; line-height: 20px; text-align: center; padding-top: 8px;
  }
  .sessions { position: absolute; left: 0; top: 205px; width: 295px; list-style: none; }
  .sessions li {
    color: var(--white); font-weight: 600; font-size: 18px; line-height: 22px;
    text-align: center; margin-bottom: 24px;
  }
  .sessions li + li { border-top: 1px solid rgba(255,255,255,0.12); padding-top: 0; }

  .price-badge {
    position: absolute; left: 612px; top: 440px; width: 330px; height: 330px;
    border-radius: 50%; background: var(--pink);
  }
  .price-inner {
    position: absolute; left: 10px; top: 10px; width: 310px; height: 310px;
    border-radius: 50%; background: var(--charcoal); text-align: center; color: var(--white);
  }
  .price-amount { font-family: "Bebas Neue", sans-serif; font-size: 76px; line-height: 70px; margin-top: 32px; }
  .price-unit { font-weight: 600; font-size: 30px; line-height: 33px; }
  .price-rule { width: 250px; height: 2px; margin: 12px auto 12px; background: linear-gradient(90deg, transparent, var(--pink), transparent); }
  .audience { font-weight: 600; font-size: 30px; line-height: 33px; }

  .venue-ribbon { position: absolute; left: 115px; top: 1093px; width: 766px; height: 85px; }
  .venue-text {
    position: absolute; left: 115px; top: 1103px; width: 766px; text-align: center; color: var(--charcoal);
  }
  .venue-text strong { display: block; font-weight: 600; font-size: 28px; line-height: 32px; }
  .venue-text span { display: block; font-weight: 500; font-size: 24px; line-height: 28px; }
  .booking {
    position: absolute; left: 100px; top: 1192px; width: 796px; text-align: center;
    color: var(--text-grey); font-weight: 500; font-size: 22px; line-height: 27px;
  }

  .footer { position: absolute; left: 0; top: 1275px; width: 996px; height: 135px; }
  .footer-shapes { position: absolute; left: 0; top: 0; width: 996px; height: 135px; }
  .footer-cta {
    position: absolute; left: 53px; top: 22px; color: var(--white);
    font-weight: 500; font-size: 28px; line-height: 37px;
  }
  .contact-phone {
    position: absolute; right: 53px; top: 28px; color: var(--white);
    font-weight: 700; font-size: 36px; line-height: 40px; display: flex; align-items: center; gap: 14px;
  }
  .contact-phone svg { width: 32px; height: 32px; }
  .contact-links {
    position: absolute; right: 53px; top: 83px; color: var(--white);
    font-size: 15px; font-weight: 500; display: flex; gap: 18px; align-items: center;
  }
  .contact-links span { display: flex; align-items: center; gap: 7px; }
  .contact-links svg { width: 14px; height: 14px; }
</style>
</head>
<body>
<main class="flyer">
  <div class="park-photo" role="img" aria-label="Woman stretching on the grass of a sunny seaside park"></div>
  <div class="class-photo" role="img" aria-label="Faint photo of a group exercise class"></div>

  <svg class="wave" viewBox="0 0 996 200" preserveAspectRatio="none" aria-hidden="true">
    <path d="M0 78 C120 40 230 30 340 50 C450 70 540 140 640 140 L996 140 L996 200 L0 200 Z" fill="#ffffff"/>
    <path d="M0 78 C120 40 230 30 340 50 C450 70 540 140 640 140 C760 140 900 110 996 90 L996 70 C900 95 760 125 640 122 C540 120 450 50 340 32 C230 14 120 30 0 65 Z" fill="#f284ad"/>
  </svg>

  <div class="logo-disc">
    <span class="logo-name">Core with Mira</span>
  </div>

  <h1 class="headline">Stretch on the Green<br>with Mira</h1>

  <h2 class="season">Classes for Summer</h2>

  <svg class="levels-ribbon" viewBox="0 0 475 67" aria-hidden="true">
    <polygon points="0,0 475,0 440,33.5 475,67 0,67" fill="#f284ad"/>
  </svg>
  <p class="levels-text">CLASSES ARE FOR BEGINNERS<br>TO ADVANCE LEVELS</p>

  <p class="benefits-intro">My Pilates classes are specially designed to help</p>
  <ul class="benefits">
    <li><svg viewBox="0 0 18 18"><circle cx="9" cy="9" r="7.5" fill="none" stroke="#4a4a4a" stroke-width="1.4"/><path d="M5.5 9 L8.2 11.6 L14.5 5" fill="none" stroke="#4a4a4a" stroke-width="1.6"/></svg>improve strength and flexibility</li>
    <li><svg viewBox="0 0 18 18"><circle cx="9" cy="9" r="7.5" fill="none" stroke="#4a4a4a" stroke-width="1.4"/><path d="M5.5 9 L8.2 11.6 L14.5 5" fill="none" stroke="#4a4a4a" stroke-width="1.6"/></svg>improve posture</li>
    <li><svg viewBox="0 0 18 18"><circle cx="9" cy="9" r="7.5" fill="none" stroke="#4a4a4a" stroke-width="1.4"/><path d="M5.5 9 L8.2 11.6 L14.5 5" fill="none" stroke="#4a4a4a" stroke-width="1.6"/></svg>reduce stress and develop control and endurance in the entire body</li>
  </ul>

  <section class="schedule">
    <p class="start-strip">CLASSES START MONDAY<br>OCTOBER 17TH</p>
    <ul class="sessions">
      <li>Monday 6pm Beginners</li>
      <li>Tuesday 6pm Intermediate</li>
      <li>Thursday 6pm<br>Intermediate/Advance</li>
      <li>Saturday 9am All fitness<br>levels</li>
    </ul>
  </section>

  <div class="price-badge">
    <div class="price-inner">
      <div class="price-amount">$15</div>
      <div class="price-unit">PER<br>SESSION</div>
      <div class="price-rule"></div>
      <div class="audience">MALES AND<br>FEMALES AGES<br>35PLUS.</div>
    </div>
  </div>

  <svg class="venue-ribbon" viewBox="0 0 766 85" aria-hidden="true">
    <polygon points="0,0 766,0 722,42.5 766,85 0,85 44,42.5" fill="#f284ad"/>
  </svg>
  <p class="venue-text">
    <strong>Classes are outside at the lovely local park</strong>
    <span>Holloway field. 83 Marangi St. Sandringham</span>
  </p>

  <p class="booking">Booking essential. Limited numbers so I can make sure the correct technique is always being followed.</p>

  <footer class="footer">
    <svg class="footer-shapes" viewBox="0 0 996 135" aria-hidden="true">
      <polygon points="418,23 996,23 996,135 475,135" fill="#4a4a4a"/>
      <polygon points="0,0 408,0 475,135 0,135" fill="#f284ad"/>
    </svg>
    <p class="footer-cta">For more info or to book<br>contact details:</p>
    <p class="contact-phone">
      <svg viewBox="0 0 32 32" aria-hidden="true"><path d="M8 3 L12 3 L14 10 L11 13 C13 18 15 20 20 22 L23 19 L30 21 L30 25 C30 28 28 30 25 30 C14 29 4 19 3 8 C3 5 5 3 8 3 Z" fill="#ffffff"/><path d="M18 4 A10 10 0 0 1 28 14" fill="none" stroke="#ffffff" stroke-width="2.2"/><path d="M18 9 A5 5 0 0 1 23 14" fill="none" stroke="#ffffff" stroke-width="2.2"/></svg>
      Mira 027358164
    </p>
    <p class="contact-links">
      <span><svg viewBox="0 0 14 14" aria-hidden="true"><circle cx="7" cy="7" r="6" fill="none" stroke="#fff" stroke-width="1.2"/><ellipse cx="7" cy="7" rx="2.6" ry="6" fill="none" stroke="#fff" stroke-width="1"/><line x1="1" y1="7" x2="13" y2="7" stroke="#fff" stroke-width="1"/></svg>www.corewithmira.net</span>
      <span><svg viewBox="0 0 14 14" aria-hidden="true"><rect x="1" y="3" width="12" height="8" fill="none" stroke="#fff" stroke-width="1.2"/><path d="M1 3 L7 8 L13 3" fill="none" stroke="#fff" stroke-width="1.2"/></svg>mira@corewithmira.net</span>
    </p>
  </footer>
</main>
</body>
</html>
```